Web Design Project

I'm looking for a web design that incorporates the content included below into a web site that is clearly for a platform as a service product that helps people build complex web information systems that also do mobile apps and integrations.
Updates

Project Deadline Extended
Reason: I would like to encourage more submissions so I'm extending the deadline. Designs submitted earlier may win due to immediate need for some collateral. We will be posting several other contests in the near future if this one goes well.

Here are some sample web sites we like quite a lot:

http://www.plovra.com
http://www.tarvenik.com/
http://www.tarvenik.com/skydock/ipaas-cloud-based-integration-demand
http://www.quellobarn.com/hybrid-it

It is really important that the first 5 graphic panels in the word document get translated into a rotating banner for the home page.

Our software integrates databases, services, social-media, security, and mobile devices, but it starts with building great web applications for the desktop and real integrated systems for businesses. We also integrate accounting, CRM, and lots of other things together - that's important.

We focus on creating one system. Please try to capture that concept. Don't deliver just mobile - we're system first, and mobile second. The goal is to help our customers merge all their systems into one.

Target Market(s)

CIOs, CTOs, Technical Decision Makers, Business People

Industry/Entity Type

Build

Requirements
Must have
• Home Page that introduces the product and what it can do for people. Product Page that shows options for the product: Platform as a Service and Licensing. Services page that shows options for Services - Virtual Development Teams and Professional Services. A Blog Page. About Us Page with location info, contact info, etc.
Nice to have
• Scrolling home page banners. Lead generation - Contact us form.

```html
<!DOCTYPE html>
<html lang="en">
<head>
<meta charset="utf-8">
<title>Embercraft – Custom Enterprise Software</title>
<link href="https://fonts.googleapis.com/css2?family=Yanone+Kaffeesatz:wght@400;600;700&family=Arimo:ital,wght@0,400;0,700;1,700&display=swap" rel="stylesheet">
<style>
:root{
  --navy:#0b2a4a;
  --navy-deep:#061a30;
  --blue:#0a9ad8;
  --heading:#0b5d9a;
  --link:#1560a8;
  --red:#e0201b;
  --grey-box:#ececec;
  --grey-line:#d6d6d6;
  --text:#444;
  --orange:#f07a1a;
  --footer:#050505;
}
*{margin:0;padding:0;box-sizing:border-box}
html,body{width:678px;height:1200px;overflow:hidden;background:#fff}
body{position:relative;font-family:"Arimo",Arial,sans-serif;font-size:9px;color:var(--text)}
.abs{position:absolute}
h2,h3,.display{font-family:"Yanone Kaffeesatz","Arial Narrow",sans-serif;font-weight:600}

/* header */
.site-header{left:0;top:0;width:678px;height:95px;background:linear-gradient(180deg,#0d3a66 0%,var(--navy) 60%,var(--navy-deep) 100%);border-bottom:2px solid #e6eef5}
.brand{left:38px;top:18px;display:flex;align-items:center;gap:10px}
.brand-mark{width:56px;height:56px;border-radius:50%;background:#fff;border:4px solid #0a1e35}
.brand-name{font-family:"Yanone Kaffeesatz",sans-serif;font-weight:700;font-size:52px;color:var(--blue);letter-spacing:1px}
.account{left:451px;top:7px;font-size:8px;color:var(--blue)}
.account span{margin-right:12px}
.search{left:531px;top:4px;width:114px;height:15px;background:#fff;border:1px solid #8fb7d8;font-size:7px;color:#999;padding:3px 5px}
.search-btn{right:0;top:0;width:14px;height:13px;background:var(--blue)}
.main-nav{left:335px;top:59px;color:#fff;font-size:9px;display:flex;gap:10px}
.main-nav b{font-weight:400}

/* banner */
.banner-band{left:0;top:97px;width:678px;height:238px;background:#0b2433}
.banner-frame{left:35px;top:112px;width:588px;height:276px;background:#fff;padding:7px}
.banner-inner{width:100%;height:100%;border:10px solid var(--blue);background:#fff;text-align:center;padding-top:8px}
.banner-title{font-family:"Yanone Kaffeesatz",sans-serif;font-weight:600;font-size:19px;line-height:20px;color:var(--blue)}
.banner-art{margin:6px auto 0;width:500px;height:186px;border-radius:6px;background:radial-gradient(ellipse at 55% 35%,#f6c94a 0%,#e86b4a 20%,#6aa8d8 40%,#dfe6ee 65%,#ffffff 85%)}
.arrow{top:242px;width:22px;height:30px;background:linear-gradient(#2aa6e8,#0a74b8);border-radius:3px}
.arrow svg{display:block;margin:8px auto}
.banner-shadow{left:130px;top:389px;width:400px;height:10px;border-radius:50%;background:radial-gradient(ellipse,rgba(0,0,0,.25),transparent 70%)}

/* info boxes */
.info-box{top:415px;height:140px;background:var(--grey-box);border:1px solid var(--grey-line);padding:14px 15px}
.info-box h2{font-size:19px;color:var(--heading);margin-bottom:8px}
.info-box h2 em{font-style:normal;color:var(--red)}
.tick-list{list-style:none}
.tick-list li{display:flex;align-items:center;gap:9px;height:22px;font-size:9px;color:var(--link)}
.tick-list li::before{content:"";width:11px;height:11px;border-radius:50%;background:radial-gradient(circle at 40% 40%,#f7c53a,var(--orange) 60%,#1c5a9e)}

/* content */
.content{left:42px;top:570px;width:390px}
.content h2{font-size:19px;color:var(--heading);margin:0 0 8px}
.content p{font-size:8.6px;line-height:11.4px;margin-bottom:16px}
.tagline{font-style:italic;font-weight:700;font-size:11px;color:#111;margin:-2px 0 8px}
.compare{display:flex;gap:62px}
.compare h3{font-size:15px;color:var(--red);margin-bottom:3px}

/* team */
.team{left:441px;top:572px;width:176px;height:434px;background:var(--grey-box);border:1px solid var(--grey-line)}
.team h2{font-size:19px;color:var(--heading);padding:6px 9px 0}
.member{position:absolute;left:0;width:100%;border-top:1px solid var(--grey-line)}
.member:first-of-type{border-top:none}
.photo{position:absolute;left:11px;width:70px;height:55px;background:linear-gradient(#7e5a4a,#3a2a24);border:1px solid #aaa}
.bio{position:absolute;left:87px;width:84px;font-size:7.4px;line-height:10px;color:var(--link)}
.role{position:absolute;left:11px;font-size:9px;color:#111}
.role b{color:var(--red);font-size:10px}

/* clients */
.clients{left:28px;top:1015px;width:617px;height:71px;background:var(--grey-box);border:1px solid var(--grey-line)}
.clients-tab{left:0;top:0;width:23px;height:71px;background:var(--orange);color:#fff;font-family:"Yanone Kaffeesatz",sans-serif;font-weight:600;font-size:12px;writing-mode:vertical-rl;transform:rotate(180deg);display:flex;align-items:center;justify-content:center;letter-spacing:1px}
.client{top:0;height:71px;display:flex;align-items:center;gap:5px;font-size:13px;font-weight:700;color:var(--navy)}
.client i{width:10px;height:10px;background:var(--navy);display:block}

/* footer */
.site-footer{left:0;top:1095px;width:678px;height:105px;background:var(--footer);border-top:1px solid #222}
.legal{left:31px;top:1132px;color:#fff;font-size:8.5px}
.social{top:1127px;width:20px;height:20px;border-radius:50%;border:1px solid #fff}
</style>
</head>
<body>

<header class="site-header abs">
  <div class="brand abs">
    <div class="brand-mark"></div>
    <div class="brand-name">Embercraft</div>
  </div>
  <div class="account abs"><span>Sign In</span><span>|</span><span>Register</span></div>
  <div class="search abs">Search<div class="search-btn abs"></div></div>
  <nav class="main-nav abs"><b>Home</b>|<b>Platform</b>|<b>Services</b>|<b>Blog</b>|<b>About Us</b>|<b>Contact Us</b></nav>
</header>

<section class="banner-band abs"></section>
<div class="arrow abs" style="left:30px"><svg width="8" height="12"><path d="M7 0L0 6l7 6z" fill="#0b2a4a"/></svg></div>
<div class="arrow abs" style="left:605px"><svg width="8" height="12"><path d="M1 0l7 6-7 6z" fill="#0b2a4a"/></svg></div>
<div class="banner-frame abs">
  <div class="banner-inner">
    <div class="banner-title">Create Custom Enterprise Software Where You Need It Connecting<br>Customers &amp; Partners To You.</div>
    <div class="banner-art" role="img" aria-label="Laptop, tablet and phone showing the platform beneath a cloud of colourful app icons"></div>
  </div>
</div>
<div class="banner-shadow abs"></div>

<section class="info-box abs" style="left:40px;width:275px">
  <h2>Embercraft, Inc - <em>Established April 2010</em></h2>
  <ul class="tick-list">
    <li>Embercraft Platform Launched - July 2012</li>
    <li>Revenue $1m in 2012, $2m+ in 2013</li>
    <li>$250k Project to Expand Market</li>
  </ul>
</section>
<section class="info-box abs" style="left:342px;width:275px">
  <h2>The Projects - <em>Plan Milestones</em></h2>
  <ul class="tick-list">
    <li>Kick-Off</li>
    <li>Simpler User Interface</li>
    <li>Self-Service Platform</li>
    <li>Training and Documentation</li>
  </ul>
</section>

<main class="content abs">
  <h2>About Us</h2>
  <p>Embercraft Technologies was founded in 2010 with the goal of enabling more people to create great custom software for the cloud than ever before possible. Since then, we've been embedding the intelligence of all the best consultants in our flagship product, the Embercraft Platform and teaching it to help build great custom systems.</p>
  <h2>Our Mission</h2>
  <p>Enable almost anyone to translate great business ideas into superior technology solutions. Keep enabling developers to do what they are great at when the time comes. Take the risk out of custom software for the cloud.</p>
  <h2>Location</h2>
  <p>Embercraft Technologies is headquartered in Brookvale, MD at the Brookvale Founders Hub (BFH). We also have staff and locations in Italy, Ukraine, and Greece and customers worldwide.</p>
  <h2 style="margin-bottom:4px">Why Us</h2>
  <div class="tagline">We Are Completely Different</div>
  <div class="compare">
    <div>
      <h3>EMBERCRAFT</h3>
      <ul class="tick-list">
        <li>Customer Owns Code and Data</li>
        <li>Intent-Oriented</li>
        <li>White Box, Deploys Anywhere</li>
        <li>Industry Standard Code</li>
      </ul>
    </div>
    <div>
      <h3>EVERYONE ELSE</h3>
      <ul class="tick-list">
        <li>Customer Owns Nothing</li>
        <li>Application / Form Oriented</li>
        <li>Black Box, Closed Cloud</li>
        <li>Proprietary</li>
      </ul>
    </div>
  </div>
</main>

<aside class="team abs">
  <h2>Meet Our Team</h2>
  <div class="member" style="top:35px;height:90px">
    <div class="photo" role="img" aria-label="Portrait of the CEO" style="top:5px"></div>
    <div class="bio" style="top:3px">Halden Educated. Norvex, Pellbright, Quorra, Votely.com, Brannick Hale Partners, Terrawell.</div>
    <div class="role" style="top:68px">Daniel R. Okafor, <b>CEO</b></div>
  </div>
  <div class="member" style="top:125px;height:103px">
    <div class="photo" role="img" aria-label="Portrait of the COO" style="top:16px"></div>
    <div class="bio" style="top:14px">Westbrook MBA. Kestrel, Pixaro, Unified Dynamo, Simvale, Notion Forge.</div>
    <div class="role" style="top:78px">Owen Talbert, <b>COO</b></div>
  </div>
  <div class="member" style="top:228px;height:104px">
    <div class="photo" role="img" aria-label="Portrait of the VP Development" style="top:16px"></div>
    <div class="bio" style="top:14px">NIT MBA. Norvex, Linkwell, Crestline Bank, Harlow Group, Marston Foods.</div>
    <div class="role" style="top:79px">Lucas Verhoef, <b>VP Development</b></div>
  </div>
  <div class="member" style="top:332px;height:102px">
    <div class="photo" role="img" aria-label="Portrait of the VP Services" style="top:14px"></div>
    <div class="bio" style="top:14px">B.S. Ashgrove College. Solari Systems, Vantrel, Norvex, Homestead Fund, Tellora.</div>
    <div class="role" style="top:77px">Martin Casale, <b>VP Services</b></div>
  </div>
</aside>

<section class="clients abs">
  <div class="clients-tab abs">CLIENTS</div>
  <div class="client abs" style="left:42px"><span>Harbor National</span><i></i></div>
  <div class="client abs" style="left:188px"><i style="border-radius:50%"></i><span>brightwave media</span></div>
  <div class="client abs" style="left:330px"><span>Campus Pulse</span></div>
  <div class="client abs" style="left:455px"><i></i><span>Mergeline</span></div>
</section>

<footer class="site-footer abs"></footer>
<div class="legal abs">© 2013, All Rights Reserved, Embercraft.com, Terms &amp; Conditions &nbsp; | &nbsp; Privacy Plicy</div>
<div class="social abs" style="left:533px;background:#2f4f8f"></div>
<div class="social abs" style="left:563px;background:#2a9ad6"></div>
<div class="social abs" style="left:593px;background:#f09a1a"></div>

</body>
</html>
```